VTM letterhead

We need the Letterhead and a page 2 which will be a simpler page - less header space for the design. Use the design you just created for the Business card. Be sure Page 2 allows for a full page of content.

Industry/Entity Type

Business

```html
<!DOCTYPE html>
<html lang="en">
<head>
<meta charset="utf-8">
<title>VTM Tech Group Letterhead</title>
<link rel="stylesheet" href="https://fonts.googleapis.com/css2?family=Gelasio:wght@400;700&family=Open+Sans:wght@400;600&display=swap">
<style>
  :root {
    --ink: #1a1a1a;
    --band: #0b0b0b;
    --accent: #c8323c;
    --paper: #ffffff;
    --backdrop: #e9e7e3;
    --body-text: #2b2b2b;
    --faint: #f1eeee;
  }
  * { box-sizing: border-box; margin: 0; padding: 0; }
  html, body {
    width: 1100px; height: 1200px; overflow: hidden;
    background: var(--backdrop);
  }
  .letterhead {
    position: absolute; left: 150px; top: 80px;
    width: 800px; height: 1040px;
    background: var(--paper);
    box-shadow: 0 4px 18px rgba(0,0,0,.18);
    overflow: hidden;
    font-family: "Gelasio", Georgia, serif;
    color: var(--body-text);
  }
  .header-band { position: absolute; left: 0; top: 0; width: 800px; height: 110px; }
  .sender-address {
    position: absolute; right: 58px; top: 40px;
    font-family: "Open Sans", Arial, sans-serif; font-weight: 600;
    font-size: 11px; line-height: 13px; color: #fff; text-align: right;
  }
  .brand {
    position: absolute; left: 72px; top: 84px;
    font-family: "Gelasio", Georgia, serif; font-weight: 700;
    font-size: 34px; color: var(--ink); letter-spacing: 1px;
    display: flex; align-items: center; gap: 10px;
  }
  .brand-mark { width: 14px; height: 14px; background: var(--accent); border-radius: 50%; }
  .letter-body { position: absolute; left: 78px; top: 196px; width: 590px; font-size: 15px; line-height: 24px; }
  .letter-date { margin-bottom: 26px; }
  .recipient { margin-bottom: 20px; line-height: 20px; }
  .recipient-name { font-weight: 700; }
  .letter-body p.paragraph { text-align: justify; hyphens: auto; margin-bottom: 24px; }
  .closing { margin-top: 44px; }
  .signature {
    width: 150px; height: 52px; margin-top: 8px;
    background: linear-gradient(90deg, #e8e8e8, #f4f4f4);
  }
  .signer-name { margin-top: -20px; font-size: 14px; }
  .watermark {
    position: absolute; right: 30px; bottom: 48px;
    font-family: "Gelasio", Georgia, serif; font-weight: 700;
    font-size: 190px; line-height: 1; color: var(--faint); letter-spacing: 4px;
  }
  .contact-row {
    position: absolute; left: 0; right: 0; bottom: 40px;
    text-align: center; font-family: "Open Sans", Arial, sans-serif;
    font-size: 11px; color: #333;
  }
  .contact-label { color: var(--accent); }
  .contact-sep { color: #999; margin: 0 8px; }
  .footer-band {
    position: absolute; left: 0; right: 0; bottom: 0; height: 30px;
    background: var(--band); color: #fff;
    font-family: "Open Sans", Arial, sans-serif; font-size: 12px;
    display: flex; align-items: center; justify-content: center;
  }
</style>
</head>
<body>
<main class="letterhead">
  <svg class="header-band" viewBox="0 0 800 110" aria-hidden="true">
    <path d="M0 52 C90 30 220 30 380 62 C520 90 650 80 800 52 L800 64 C650 92 520 102 380 76 C220 46 90 46 0 70 Z" fill="var(--accent)"/>
    <path d="M0 0 H800 V52 C650 80 520 90 380 62 C220 30 90 30 0 52 Z" fill="var(--band)"/>
  </svg>
  <div class="sender-address">2250 Harbor Ridge Road, Suite 310<br>Westbrook, MD 20990</div>
  <div class="brand"><span class="brand-mark"></span>VTM Tech Group</div>

  <section class="letter-body">
    <p class="letter-date">December 23, 2025</p>
    <div class="recipient">
      <div class="recipient-name">Martin Cole</div>
      <div>General Manager</div>
      <div>Northfield Supply Co</div>
    </div>
    <p class="paragraph">Lorem ipsum dolor sit amet, consectetur adipiscing elit. Donec orci purus, luctus vitae dignissim eu, iaculis sed purus. Vivamus faucibus, ipsum nec aliquet viverra, leo mauris condimentum ligula, sit amet sagittis enim ligula quis arcu. Nam egestas tortor id nisi porttitor mattis. In tortor ante, ultricies in suscipit a, tempus non massa. Vivamus et auctor mi. Fusce vel massa nulla. Phasellus nec eros mauris, et scelerisque orci. Donec malesuada orci vitae nulla accumsan porta a id massa. Quisque accumsan iaculis magna sit amet fringilla. Maecenas consequat, magna eget tincidunt semper, odio nibh rutrum mi, id feugiat ante nisi eu risus. Vestibulum nunc orci, ultricies in mi.</p>
    <p class="paragraph">Quisque scelerisque sagittis nulla at porttitor. Mauris a justo et tellus interdum tristique. Sed id augue vitae urna euismod commodo aliquet a quam. Pellentesque arcu velit, cursus et malesuada ut, rutrum nisi iaculis consequat et diam. Nullam erat sem, rhoncus id ullamcorper vitae, rhoncus et arcu. In ultricies ultricies nulla, ut rutrum nisi iaculis at. Donec eu magna a metus ornare faucibus. Fusce aliquet faucibus ultricies. Morbi semper, est id tincidunt gravida, sem arcu adipiscing lacus, ac bibendum nulla leo eu purus. Quisque nec diam sed risus consectetur a ccumsan quis quis nibh. Vestibulum id purus lorem.</p>
    <p class="closing">Ipsum dolor,</p>
    <div class="signature" role="img" aria-label="Handwritten signature"></div>
    <p class="signer-name">Jane Ray Porter</p>
  </section>

  <div class="watermark" aria-hidden="true">VTM</div>

  <div class="contact-row">
    <span class="contact-label">Phone:</span> 410.555.0182<span class="contact-sep">|</span><span class="contact-label">Fax:</span> 410.555.0147<span class="contact-sep">|</span><span class="contact-label">Email:</span> nina@vtmtechgroup.com<span class="contact-sep">|</span><span class="contact-label">Web:</span> www.vtmtechgroup.com
  </div>
  <div class="footer-band">Woman Owned Small Business</div>
</main>
</body>
</html>
```